Halmi Rékas Physiotherapy Business Card Vienna

We need a business card design for a newly created Physiotherapy company based in Vienna Austria.
We seek a simple, modern, minimalist design without too much color variation. The font should look young/fresh, but definitely not childish or so. Since we are a starting Business, we currently haven't got a logo, if you feel like a logo would fit your design, feel free to use one, but it's not necessary.
Target Market(s)
Healthcare, young and elderly people with mobility issues
Industry/Entity Type
Health And Wellness
Contact Information for Business Card
Name: Réka Halmi
Title description: Physiotherapist
Phone num: +43 664 5290 4116
e-mail: reka.praxis@examplemail.net
Colors
Designer to choose colors to be used in the design.
Requirements
Must have
- Final design language must be in German, basically, the Title Description needs to be "Physiotherapeutin" the other details remain as in the English Language.
Nice to have
- Simple, modern, minimalist design
Should not have
- too many colors, Obvious use of a skeleton, skull, spline

```html
<!DOCTYPE html>
<html lang="de">
<head>
<meta charset="utf-8">
<title>Réka Halmi – Visitenkarte</title>
<link rel="stylesheet" href="https://fonts.googleapis.com/css2?family=Antonio:wght@300;400&family=Montserrat:wght@400&display=swap">
<style>
  :root {
    --backdrop: #959595;
    --paper: #f4f4f2;
    --ink: #4a4a4a;
    --accent: #2ebfa5;
    --edge: #12997f;
    --card-dark: #2b2b2b;
  }
  * { box-sizing: border-box; margin: 0; padding: 0; }
  html, body {
    width: 1200px;
    height: 1147px;
    overflow: hidden;
    background: var(--backdrop);
  }
  .stage {
    position: relative;
    width: 1200px;
    height: 1147px;
  }
  .card {
    position: absolute;
    width: 780px;
    height: 446px;
    border-bottom: 5px solid var(--edge);
  }
  .card--front {
    left: 210px;
    top: 90px;
    background: var(--paper);
  }
  .card--back {
    left: 210px;
    top: 610px;
    background: var(--card-dark);
  }
  .card__pattern {
    position: absolute;
    inset: 0;
    background: linear-gradient(135deg, #2e2e2e 0%, #262626 100%);
  }
  .name {
    position: absolute;
    left: 64px;
    top: 72px;
    font-family: "Antonio", "Arial Narrow", sans-serif;
    font-weight: 400;
    font-size: 56px;
    letter-spacing: 5px;
    color: var(--ink);
    text-transform: uppercase;
    line-height: 1;
  }
  .title {
    position: absolute;
    right: 64px;
    top: 170px;
    font-family: "Antonio", "Arial Narrow", sans-serif;
    font-weight: 400;
    font-size: 40px;
    letter-spacing: 3px;
    color: var(--accent);
    text-transform: uppercase;
    line-height: 1;
    white-space: nowrap;
  }
  .contact {
    position: absolute;
    left: 64px;
    bottom: 62px;
    list-style: none;
    font-family: "Montserrat", Arial, sans-serif;
    font-size: 18px;
    color: var(--ink);
  }
  .contact__item {
    display: flex;
    align-items: center;
    gap: 14px;
    line-height: 32px;
  }
  .contact__icon {
    width: 17px;
    height: 17px;
    flex: none;
  }
</style>
</head>
<body>
<main class="stage">
  <section class="card card--front" aria-label="Vorderseite der Visitenkarte">
    <h1 class="name">Réka Halmi</h1>
    <p class="title">Physiotherapeutin</p>
    <ul class="contact">
      <li class="contact__item">
        <svg class="contact__icon" viewBox="0 0 24 24" aria-hidden="true">
          <path fill="var(--accent)" d="M6.6 10.8c1.4 2.8 3.8 5.1 6.6 6.6l2.2-2.2c.3-.3.7-.4 1-.2 1.1.4 2.3.6 3.6.6.6 0 1 .4 1 1V20c0 .6-.4 1-1 1C10.6 21 3 13.4 3 4c0-.6.4-1 1-1h3.5c.6 0 1 .4 1 1 0 1.3.2 2.5.6 3.6.1.3 0 .7-.2 1L6.6 10.8z"/>
        </svg>
        <span>+43 664 5290 4116</span>
      </li>
      <li class="contact__item">
        <svg class="contact__icon" viewBox="0 0 24 24" aria-hidden="true">
          <rect x="2.5" y="5" width="19" height="14" fill="none" stroke="var(--accent)" stroke-width="1.8"/>
          <path d="M2.5 5l9.5 8 9.5-8" fill="none" stroke="var(--accent)" stroke-width="1.8"/>
        </svg>
        <span>reka.praxis@examplemail.net</span>
      </li>
    </ul>
  </section>

  <section class="card card--back" aria-label="Rückseite der Visitenkarte">
    <div class="card__pattern" role="img" aria-label="Dark background with a fine grey zigzag line pattern"></div>
  </section>
</main>
</body>
</html>
```